Price Package PDF - 2 page PDF of stylized price packages for property management firm

Looking for a 2 x A4 page PDF for our two price packages.
I would like this to be in similar style to our website www.harbourlanerentals.com.au
I have attached an example. But would like mine to be a little more stylish and modern, preferably using design similar to our website.
Words and images also attached

Target Market(s)

investment property owners, male and female, aged 30-60

Industry/Entity Type

Real Estate

Font styles to use
Sans Serif

Requirements
Must have
• split two packages onto seperate A4 pages (See example file attached)
• Contact info:
• Website: www.harbourlanerentals.com.au
• email: info@harbourlanerentals.com.au
• Phone: Tom Willard 0438 216 907, Marika Dunstan 0419 572 046
• Office Address: Suite 7, 12-14 Carrow Parade, Dee Why NSW 2099
Nice to have
• I would like to use any of the pictures provided or images of modern residential property interior or of Sydney's Northern Beaches.

```html
<!DOCTYPE html>
<html lang="en">
<head>
<meta charset="utf-8">
<title>Harbour Lane Rentals – All Inclusive Package</title>
<link rel="stylesheet" href="https://fonts.googleapis.com/css2?family=Source+Sans+3:wght@300;400;600;700&display=swap">
<style>
:root{
  --teal:#2c8593;
  --teal-dark:#1f6872;
  --teal-light:#3ec3cc;
  --teal-pale:#d7eef0;
  --grey:#e4e5e6;
  --ink:#3b3b3b;
  --white:#ffffff;
}
*{margin:0;padding:0;box-sizing:border-box}
html,body{width:848px;height:1200px;overflow:hidden;background:var(--white)}
body{font-family:"Source Sans 3",Arial,sans-serif;color:var(--ink)}
.page{position:relative;width:848px;height:1200px;overflow:hidden;background:var(--white)}

.hero{position:absolute;left:0;top:0;width:848px;height:486px;
  background:linear-gradient(180deg,#1f7fc4 0%,#5aa6d6 30%,#8fa6a8 52%,#5f7a4a 74%,#3e5a33 100%)}
.brand{position:absolute;left:17px;top:60px;display:flex;align-items:center;gap:12px;
  color:var(--white);font-weight:700;font-size:34px;letter-spacing:.3px;white-space:nowrap}
.brand-mark{width:14px;height:14px;background:var(--white)}

.package-band{position:absolute;left:0;top:484px;width:848px;height:57px;background:var(--teal);
  color:var(--white);font-weight:300;font-size:39px;line-height:57px;padding-left:20px;white-space:nowrap}

.backdrop{position:absolute;left:0;top:0}

.includes{position:absolute;left:0;top:545px;width:848px}
.includes h2{position:absolute;left:94px;top:0;color:var(--teal);font-size:18px;font-weight:700;line-height:24px}
.feature-list{list-style:none;position:absolute;left:0;top:25px;font-size:16px;line-height:22px;white-space:nowrap}
.feature-list li{position:relative}
.feature-list li::before{content:"•";margin-right:6px}
.feature-list .wrap{line-height:19px;margin-bottom:3px}
.feature-list .wrap .cont{display:block;padding-left:12px}

.contact{position:absolute;left:18px;top:937px;color:var(--white);white-space:nowrap}
.contact h3{font-size:16px;font-weight:700;line-height:29px;margin-bottom:7px}
.contact p{font-size:14.5px;line-height:19px}
.contact .label{font-size:11.5px;line-height:14px;margin-top:5px}
.contact .name{font-weight:700;font-size:12.5px;line-height:22px}

.rate-head{position:absolute;left:214px;top:958px;width:558px;height:28px;background:var(--teal-dark);
  color:var(--white);font-weight:700;font-size:16px;line-height:28px;padding-left:14px;
  clip-path:polygon(0 0,97% 0,100% 100%,3% 100%)}
.rate-row{position:absolute;height:27px;width:562px;background:var(--white);border-bottom:4px solid var(--teal-light);
  font-size:15.5px;line-height:24px;color:var(--ink);white-space:nowrap}
.rate-row b{font-weight:700}
.rate-row.main{font-weight:600;font-size:16px;height:32px;line-height:30px;border-bottom-color:var(--teal-pale)}
.rate-row .big{font-size:28px;font-weight:700;vertical-align:-2px}
.rate-row .small{font-weight:400;font-size:15.5px}
</style>
</head>
<body>
<main class="page">
  <div class="hero" role="img" aria-label="Photo of a modern two-storey coastal home with glass balconies against a blue sky and garden"></div>
  <div class="brand"><span class="brand-mark"></span>HARBOUR LANE RENTALS</div>
  <h1 class="package-band">All Inclusive Package:</h1>

  <svg class="backdrop" width="848" height="1200" viewBox="0 0 848 1200" aria-hidden="true">
    <polygon points="0,541 85,541 242,936 0,936" fill="var(--grey)"/>
    <polygon points="0,966 250,966 300,1200 0,1200" fill="var(--teal)"/>
    <polygon points="0,936 242,936 256,966 0,966" fill="var(--teal-dark)"/>
    <polygon points="242,936 292,936 270,966 256,966" fill="var(--teal-light)"/>
  </svg>

  <section class="includes">
    <h2>Includes:</h2>
    <ul class="feature-list">
      <li style="margin-left:103px">Securing Tenant</li>
      <li style="margin-left:107px">Reference/Database Checking</li>
      <li style="margin-left:111px">Lease Preparation and Signing</li>
      <li style="margin-left:118px">Direct Debit rent collection</li>
      <li style="margin-left:123px">Zero arrears policy management</li>
      <li style="margin-left:128px">Payment of Rates and levies</li>
      <li style="margin-left:135px">Insurance management</li>
      <li style="margin-left:148px">Coordination of all repairs and maintenance</li>
      <li style="margin-left:148px">Regular rent reviews and renewals</li>
      <li class="wrap" style="margin-left:154px">Detailed ingoing, ongoing and outgoing inspections with photos and<span class="cont">videos – viewable through your personal Landlord portal</span></li>
      <li style="margin-left:171px">Bond management – lodging and refunding</li>
      <li style="margin-left:178px">Electronic monthly and EOFY statements</li>
      <li style="margin-left:187px">Annual scheduled maintenance report</li>
      <li style="margin-left:194px">Regulation/compliance management</li>
      <li style="margin-left:202px">Tribunal Representation</li>
    </ul>
  </section>

  <section class="contact">
    <h3>Contact info:</h3>
    <p>Suite 7, 12-14 Carrow Parade,<br>Dee Why NSW 2099</p>
    <p class="label">phone:</p>
    <p class="name">Tom Willard&nbsp; 0438 216 907</p>
    <p class="name">Marika Dunstan&nbsp; 0419 572 046</p>
    <p class="label">email:</p>
    <p>info@harbourlanerentals.com.au</p>
    <p class="label">website:</p>
    <p>www.harbourlanerentals.com.au</p>
  </section>

  <section class="rates">
    <div class="rate-head">All Inclusive Package:</div>
    <div class="rate-row main" style="left:218px;top:987px;padding-left:12px"><b>Management Rate:</b>&nbsp; <span class="big">10%</span> <span class="small">+GST of rental income</span></div>
    <div class="rate-row" style="left:228px;top:1021px;padding-left:14px">Letting Fee:&nbsp; No Charge</div>
    <div class="rate-row" style="left:238px;top:1048px;padding-left:16px">Advertising:&nbsp; No Charge</div>
    <div class="rate-row" style="left:249px;top:1075px;padding-left:16px">Professional Photography: <b>$199 (inc GST)</b> 4 x Photos</div>
    <div class="rate-row" style="left:259px;top:1102px;padding-left:18px">Statements:&nbsp; No Charge</div>
    <div class="rate-row" style="left:270px;top:1129px;padding-left:18px">Lease Preparation:&nbsp; No Charge</div>
    <div class="rate-row" style="left:281px;top:1156px;padding-left:20px">Renewal Fees:&nbsp; No Charge</div>
  </section>
</main>
</body>
</html>
```